Dental Brochure for New Dental Advertising Company

Please create a beautiful brochure design based on the rough outlines provided. I'd like for the brochure design to be modern with strong graphic usage and clean fonts. Large pictures of pretty people smiling.

Feel free to arrange items as you see fit. I have attached a historical brochure for layout reference mainly- I do need mailing panel laid out similarly as KRDM will need the indicia in the top right corner with address box below and return address info next to indicia.

Id like a format that I can use to edit in Adobe programs in the future.

The size of layout is 9 "x 15" that folds into a 9" x 5" brochure.

Target Market(s)

Dental Consumer

Industry/Entity Type

Dental

Requirements
Nice to have
• Dentists love big pictures of people smiling. Simple layout with easy to read content.

```html
<!DOCTYPE html>
<html lang="en">
<head>
<meta charset="utf-8">
<title>Maple Grove Family Dental – Tri-fold Brochure</title>
<link rel="stylesheet" href="https://fonts.googleapis.com/css2?family=Tinos:ital,wght@0,400;0,700;1,400;1,700&family=Arimo:wght@400;700&display=swap">
<style>
:root{
  --purple:#46308c;
  --purple-dark:#36246f;
  --green:#3aa64b;
  --green-dark:#2f8a45;
  --teal:#5fc2b5;
  --sky:#d4ebf7;
  --sky-light:#eef7fc;
  --ink:#333;
  --white:#fff;
  --serif:'Tinos', 'Times New Roman', serif;
  --sans:'Arimo', Arial, sans-serif;
}
*{box-sizing:border-box;margin:0;padding:0}
html,body{width:755px;height:1200px;overflow:hidden;background:#fff}
.canvas{position:relative;width:755px;height:1200px;background:#fff}
.spread{position:absolute;left:0;width:755px;height:533px;overflow:hidden;background:linear-gradient(160deg,var(--sky) 0%,var(--white) 45%,var(--sky-light) 100%);box-shadow:0 2px 8px rgba(0,0,0,.12)}
.spread--outside{top:40px}
.spread--inside{top:630px}
.layer{position:absolute;left:0;top:0;width:755px;height:533px}
.block{position:absolute;text-align:center}
.heading{font-family:var(--serif);color:var(--purple);font-weight:700;line-height:1.15}
.subhead{font-family:var(--serif);color:var(--green);font-weight:700;font-size:9px;line-height:1.3}
.body{font-family:var(--sans);color:var(--ink);font-size:7.5px;line-height:1.3}
.fine{font-family:var(--sans);color:var(--ink);font-size:5.5px;line-height:1.3}
.photo{position:absolute}
.photo--round{border-radius:50%;border:3px solid var(--white);box-shadow:0 0 0 2px var(--teal)}
.brand{position:absolute;display:flex;align-items:center;gap:6px;font-family:var(--serif);font-weight:700;color:var(--purple);font-size:14px;line-height:1.05}
.brand__dot{width:26px;height:26px;border-radius:50%;background:var(--green);flex:none}
.social{display:flex;justify-content:center;gap:6px;margin-top:8px}
.social span{width:12px;height:12px;border-radius:50%;background:var(--purple)}
.social span + span{background:#e0483a}
.mailing{position:absolute;transform:rotate(-90deg);transform-origin:left top;font-family:var(--sans);color:var(--ink)}
.indicia{position:absolute;left:285px;top:30px;width:30px;height:32px;border:1px solid #999;background:#fff;font-family:var(--sans);font-size:4px;line-height:1.2;padding:2px;text-align:center}
.badge{position:absolute;left:539px;top:320px;width:172px;height:152px;border-radius:44px;background:var(--white);border:4px solid var(--green);box-shadow:0 2px 6px rgba(0,0,0,.25);text-align:center;padding-top:18px}
.badge__title{font-family:var(--serif);font-style:italic;color:var(--purple);font-size:14px;line-height:1.2}
.badge__rule{width:90px;height:1px;background:#777;margin:8px auto 6px}
.url{position:absolute;font-family:var(--serif);color:var(--white);font-size:9.5px}
.card{position:absolute;left:528px;top:95px;width:203px;height:400px;background:var(--white);border-radius:12px;box-shadow:0 2px 6px rgba(0,0,0,.2);text-align:center;padding:18px 10px 0}
.cta{display:inline-block;background:var(--green);color:var(--white);font-family:var(--serif);font-weight:700;font-size:8px;padding:5px 14px;border-radius:4px;margin:12px 0 16px}
.bullets{list-style:none;text-align:left}
.bullets li{font-family:var(--sans);font-size:7px;color:var(--ink);line-height:1.9}
</style>
</head>
<body>
<div class="canvas">

  <!-- OUTSIDE SPREAD -->
  <section class="spread spread--outside">
    <svg class="layer" viewBox="0 0 755 533" aria-hidden="true">
      <defs>
        <linearGradient id="bandOut" x1="0" x2="1">
          <stop offset="0" stop-color="#3aa64b"/>
          <stop offset=".45" stop-color="#2f7f78"/>
          <stop offset=".75" stop-color="#46308c"/>
          <stop offset="1" stop-color="#3a2680"/>
        </linearGradient>
      </defs>
      <path d="M0 360 C 120 330, 250 430, 420 445 C 560 455, 690 300, 755 150 L755 200 C 700 320, 560 470, 420 470 C 250 470, 120 380, 0 395 Z" fill="#bfe3f4"/>
    </svg>

    <!-- Panel 1 -->
    <h2 class="block heading" style="left:10px;top:30px;width:232px;font-size:16px">Stay Healthy With<br>Regular Cleanings!</h2>
    <p class="block body" style="left:12px;top:82px;width:228px">Cleanings Help Protect You &amp; Your Family From:<br>Heart Disease • Strokes • The Worsening of Asthma<br>The Worsening of Diabetes • Helps Ensure Healthy<br>Pregnancy Reduces Chances of Alzheimer’s • Reduces<br>Chances of Dementia</p>
    <p class="block body" style="left:12px;top:136px;width:228px">Sources: national health institutes, university dental<br>schools, peer-reviewed dental and medical<br>journals &amp; many more</p>
    <p class="block body" style="left:12px;top:170px;width:228px">copyright © 2022 brightpath media, inc.<br>all rights reserved</p>
    <h2 class="block heading" style="left:10px;top:203px;width:232px;font-size:15px">Emergency Dental<br>Care Available Today!</h2>
    <div class="photo" role="img" aria-label="Photo of a smiling father with his children" style="left:0;top:248px;width:255px;height:170px;background:linear-gradient(120deg,#e6d3c2,#b98e6e 45%,#eadbcf 75%,#f4eee9)"></div>

    <!-- Panel 2 : mailing -->
    <div class="indicia">PRSRT STD POSTAGE PAID KRDM</div>
    <div class="mailing" style="left:270px;top:200px;width:170px">
      <div style="font-family:var(--serif);font-weight:700;color:var(--purple);font-size:9px">Maple Grove Family Dental</div>
      <div style="font-size:8px;line-height:1.35;margin-top:2px">18 Linden Street, Suite 210,<br>Maple Grove, NJ 07100<br>555-204-7710<br>MapleGroveFamilyDental.example</div>
    </div>
    <div class="mailing" style="left:396px;top:185px;font-size:7px">MAILING ADDRESS HERE</div>
    <div class="mailing" style="left:438px;top:205px;width:180px;font-size:4.5px;line-height:1.4">Return service requested. Please recycle this mailer after reading.</div>

    <h2 class="block heading" style="left:252px;top:234px;width:252px;font-size:13.5px;font-style:italic">We Love Your Insurance!</h2>
    <p class="block body" style="left:252px;top:252px;width:252px">Most insured patients pay nothing out-of-pocket<br>for the services below:</p>
    <p class="block" style="left:252px;top:277px;width:252px;font-family:var(--serif);font-size:9.5px;line-height:1.35;color:var(--ink)">Brighter, Whiter Cleaning for Adults<br>Cleaning &amp; Exam for Children<br>Exam for Adults<br><b>FREE</b> Second Opinion Evaluation<span class="social"><span></span><span></span></span></p>

    <!-- Panel 3 : cover -->
    <div class="photo" role="img" aria-label="Photo of a smiling mother with her young daughter" style="left:482px;top:100px;width:273px;height:330px;background:linear-gradient(135deg,#f2ede8,#d9b08c 40%,#b07a52 60%,#efe4da)"></div>

    <svg class="layer" viewBox="0 0 755 533" aria-hidden="true">
      <path d="M0 395 C 120 380, 250 470, 420 470 C 560 470, 700 320, 755 200 L755 533 L0 533 Z" fill="url(#bandOut)"/>
      <path d="M755 175 C 700 260, 620 300, 520 533 L755 533 Z" fill="#3d2983"/>
      <line x1="252" y1="0" x2="252" y2="533" stroke="#fff" stroke-opacity=".25"/>
      <line x1="503" y1="0" x2="503" y2="533" stroke="#fff" stroke-opacity=".25"/>
    </svg>

    <div class="photo photo--round" role="img" aria-label="Photo of a dental hygienist treating a smiling patient" style="left:41px;top:388px;width:130px;height:130px;background:linear-gradient(135deg,#e7f3fb,#9cc8de 50%,#d7b59a)"></div>
    <div class="photo photo--round" role="img" aria-label="Photo of a dentist examining a young woman" style="left:294px;top:375px;width:150px;height:150px;background:linear-gradient(135deg,#dfeef8,#8fb9d3 50%,#c99a7c)"></div>

    <div class="brand" style="left:551px;top:38px"><span class="brand__dot"></span><span>Maple Grove<br>Family Dental</span></div>
    <div class="badge">
      <div class="badge__title">A 20-Year<br>Maple Grove Tradition<br>of Trusted &amp; Caring<br>Dental Excellence!</div>
      <div class="badge__rule"></div>
      <div class="body">Welcome Weekdays as<br>Late as 6pm &amp; Saturdays!</div>
    </div>
    <div class="url" style="left:503px;top:500px;width:252px;text-align:center">www.maplegrovesmiles.example</div>
  </section>

  <!-- INSIDE SPREAD -->
  <section class="spread spread--inside">
    <svg class="layer" viewBox="0 0 755 533" aria-hidden="true">
      <defs>
        <linearGradient id="bandIn" x1="0" x2="1">
          <stop offset="0" stop-color="#3aa64b"/>
          <stop offset=".45" stop-color="#2f8a55"/>
          <stop offset=".75" stop-color="#2e6a72"/>
          <stop offset="1" stop-color="#3f3088"/>
        </linearGradient>
      </defs>
      <path d="M270 0 C 380 30, 470 70, 510 150 L 505 533 L755 533 L755 0 Z" fill="#46308c"/>
      <path d="M0 385 C 90 360, 190 380, 260 410 C 340 445, 430 450, 505 440 L505 460 C 420 470, 330 465, 260 430 C 190 400, 90 385, 0 405 Z" fill="#bfe3f4"/>
      <path d="M0 405 C 90 385, 190 400, 260 430 C 330 465, 420 470, 505 460 L505 533 L0 533 Z" fill="url(#bandIn)"/>
      <line x1="252" y1="0" x2="252" y2="533" stroke="#fff" stroke-opacity=".25"/>
    </svg>

    <!-- Panel 1 -->
    <div class="photo" role="img" aria-label="Photo of a smiling man in the dental chair with a hygienist" style="left:-3px;top:-3px;width:280px;height:180px;border-bottom-right-radius:140px 180px;border:3px solid var(--teal);background:linear-gradient(120deg,#cfe6f3,#6fa7c9 40%,#e2c3a8 70%,#f4ece4)"></div>
    <h2 class="block heading" style="left:10px;top:188px;width:232px;font-size:16px">Stay Healthy With<br>Regular Cleanings!</h2>
    <p class="block subhead" style="left:10px;top:233px;width:232px">Cleanings Help Protect You &amp;<br>Your Family From:</p>
    <p class="block body" style="left:10px;top:263px;width:232px">Heart Disease • Strokes • The Worsening of Asthma<br>The Worsening of Diabetes • Helps Ensure Healthy<br>Pregnancy Reduces Chances of Alzheimer’s • Reduces<br>Chances of Dementia</p>
    <p class="block body" style="left:10px;top:310px;width:232px">Sources: national health institutes, university dental<br>schools, peer-reviewed dental and medical<br>journals &amp; many more</p>
    <p class="block fine" style="left:10px;top:352px;width:232px">copyright © 2022 brightpath media, inc. all rights reserved</p>
    <h2 class="block heading" style="left:10px;top:406px;width:232px;font-size:19px;color:#e6e0f5;font-weight:400">We Love Kids &amp;<br>Families</h2>
    <p class="block" style="left:10px;top:468px;width:232px;font-family:var(--serif);font-size:14px;line-height:1.35;color:#e6e0f5">Welcome Weekdays<br>as Late as 6pm &amp; Saturdays!</p>

    <!-- Panel 2 -->
    <h2 class="block heading" style="left:262px;top:84px;width:232px;font-size:15.5px;font-weight:400">Trusted, Personalized<br>&amp; Affordable Dental Care<br>for Your Whole Family</h2>
    <p class="block subhead" style="left:262px;top:154px;width:232px">Cleanings Help Protect You &amp;<br>Your Family From:</p>
    <ul class="bullets" style="position:absolute;left:281px;top:182px;width:210px">
      <li>• Low-Cost Dental Coverage for Uninsured Patients</li>
      <li>• Convenient Hours ~ Never Miss Work or School!</li>
      <li>• 0% Financing Available</li>
    </ul>
    <div class="brand" style="left:312px;top:238px;font-size:12px"><span class="brand__dot" style="width:22px;height:22px"></span><span>Maple Grove<br>Family Dental</span></div>
    <h2 class="block heading" style="left:262px;top:294px;width:232px;font-size:15px;font-weight:400">Walk In! You’re<br>Always Welcome!</h2>
    <p class="block subhead" style="left:262px;top:345px;width:232px;font-size:8px">18 Linden Street, Suite 210 • Maple Grove</p>
    <p class="block fine" style="left:262px;top:362px;width:232px;font-size:6px">We are located on Linden Street &amp; Oak Road, just off of<br>Route 4, on the 2nd floor of the Hollis &amp; Reed building.</p>
    <p class="block heading" style="left:262px;top:462px;width:232px;font-size:21px;color:#fff;font-weight:400">555-204-7710</p>
    <p class="url" style="left:262px;top:497px;width:232px;text-align:center;font-size:9px;font-weight:700">www.MapleGroveFamilyDental.example</p>

    <!-- Panel 3 -->
    <h2 class="block heading" style="left:512px;top:30px;width:236px;font-size:20px;color:#fff;font-weight:400">One Office for All<br>Your Dental Needs</h2>
    <div class="card">
      <p class="body" style="font-size:6.8px">The Latest Procedures, Instruments &amp;<br>Techniques Gentle Private-Practice Dentists<br>• Sealants &amp; Fluoride Treatments<br>Low-Radiation Digital X-Rays •<br>Laser-Assisted Dental Treatment Infrared<br>Cavity Diagnosis • Root Canal Treatments<br>Bridges &amp; Implants • Dentures • FillaLift •<br>ContourOne We Offer Nitrous Oxide &amp; Free<br>Whitening For Life!</p>
      <h3 class="heading" style="font-size:15px;margin-top:12px">Cosmetic Dentistry Can<br>Change Your Life!</h3>
      <p class="body" style="font-size:6.8px;margin-top:10px">Mercury-Free Dentistry • BrightGlow Teeth<br>Whitening Crowns • Veneers</p>
      <span class="cta">Call us today for more details.</span>
      <h3 class="heading" style="font-size:12.5px">Reduce Wrinkles With<br>SmoothLine® &amp; DermaFill®!</h3>
      <p class="body" style="font-size:6.8px;margin-top:12px">Look Younger • Takes Only 10 Minutes<br>No Recovery Time</p>
      <p class="body" style="font-size:6.8px;margin-top:18px">Restore youthful contours to the skin &amp; smooth<br>away moderate to severe wrinkles &amp; folds.<br>Call today for your appointment.</p>
    </div>
  </section>

</div>
</body>
</html>
```